Business Card Design Project

I need some business cards with the logo you did for us (attached)
I am looking for a coulourful yet serious business card

We do market research
on the back I want the logo

on the front my name : Corinne Valdessac
position : Manager
address : Brume Analytica Sarl - 27 Rue des tanneurs
1847 Glarency - Switzerland
corinne.valdessac@brumeanalytica.ch
Tel : +4122 934 07 58
Mob France :+33 671 42 8356
Mob Italy +39 347 520 8163

The tree of the logo could also be used alone

THE BACKGROUND COLOR ON THE FRONT HAS TO BE WHITE, ON THE BACK YU CAN TRY OHER COLOUR BUT HOMOGENEOUS (NOT EXPENSIVE TO PRINT)

Target Market(s)

multinational companies or other market research companies

Industry/Entity Type

Market Research

Requirements
Must have
• logo on the back
and all the info above

```html
<!DOCTYPE html>
<html lang="en">
<head>
<meta charset="utf-8">
<title>Brume Analytica – Business Card</title>
<link rel="stylesheet" href="https://fonts.googleapis.com/css2?family=Sofia&family=Arimo:wght@400;700&display=swap">
<style>
  :root {
    --paper: #ffffff;
    --name-red: #a3272f;
    --brand-pink: #d6245e;
    --soft-grey: #707070;
    --label-green: #19a24a;
    --value-brown: #6b3a2e;
    --email-grey: #555555;
    --divider: #9a9a9a;
    --mark-tint: #f4cbd8;
  }
  * { margin: 0; padding: 0; box-sizing: border-box; }
  html, body { width: 1200px; height: 1200px; overflow: hidden; background: var(--paper); }
  .canvas { position: relative; width: 1200px; height: 1200px; background: var(--paper); }

  .card-front, .card-back { position: absolute; left: 0; width: 1200px; }
  .card-front { top: 0; height: 607px; }
  .card-back { top: 609px; height: 591px; }
  .card-divider { position: absolute; left: 0; top: 607px; width: 1200px; height: 2px; background: var(--divider); }

  .script { font-family: "Sofia", cursive; line-height: 1; position: absolute; left: 52px; white-space: nowrap; }
  .holder-name { top: 88px; font-size: 68px; color: var(--name-red); }
  .holder-role { top: 168px; font-size: 46px; color: var(--soft-grey); }
  .company-name { top: 268px; font-size: 56px; color: var(--brand-pink); }
  .address-line { font-size: 48px; color: var(--soft-grey); }
  .address-line.street { top: 336px; }
  .address-line.city { top: 392px; }

  .tree-mark { position: absolute; left: 883px; top: 105px; }

  .contact-list { position: absolute; right: 80px; top: 380px; text-align: right; font-family: "Arimo", Arial, sans-serif; }
  .contact-row { white-space: nowrap; color: var(--value-brown); }
  .contact-row .label { color: var(--label-green); }
  .contact-row.tel { font-size: 34px; line-height: 42px; }
  .contact-row.mobile { font-size: 27px; line-height: 40px; }
  .contact-row.mobile .label { font-weight: 700; }
  .contact-row.email { font-size: 27px; line-height: 44px; color: var(--email-grey); }

  .brand-lockup { position: absolute; left: 0; top: 0; width: 1200px; height: 591px; }
  .brand-dot { position: absolute; left: 465px; top: 110px; }
  .brand-wordmark {
    position: absolute; left: 0; width: 1200px; top: 385px; text-align: center;
    font-family: "Arimo", Arial, sans-serif; font-weight: 400; font-size: 104px; line-height: 1;
    color: var(--brand-pink); white-space: nowrap;
  }
</style>
</head>
<body>
<main class="canvas">
  <section class="card-front">
    <h1 class="script holder-name">Corinne Valdessac</h1>
    <p class="script holder-role">Manager</p>
    <p class="script company-name">Brume Analytica Sarl</p>
    <p class="script address-line street">27 Rue des tanneurs</p>
    <p class="script address-line city">1847 Glarency - Switzerland</p>

    <svg class="tree-mark" width="170" height="170" viewBox="0 0 170 170" role="img" aria-label="Company mark">
      <circle cx="85" cy="85" r="80" fill="var(--mark-tint)"/>
    </svg>

    <div class="contact-list">
      <p class="contact-row tel"><span class="label">Tel:</span> +4122 934 07 58</p>
      <p class="contact-row mobile"><span class="label">Mob Italy:</span> +39 347 520 8163</p>
      <p class="contact-row mobile"><span class="label">Mob France:</span> +33 671 42 8356</p>
      <p class="contact-row email">corinne.valdessac@brumeanalytica.ch</p>
    </div>
  </section>

  <div class="card-divider"></div>

  <section class="card-back">
    <div class="brand-lockup">
      <svg class="brand-dot" width="270" height="270" viewBox="0 0 270 270" role="img" aria-label="Company mark">
        <circle cx="135" cy="135" r="130" fill="var(--mark-tint)"/>
      </svg>
      <p class="brand-wordmark">brume analytica</p>
    </div>
  </section>
</main>
</body>
</html>
```